Smart, intuitive SaaS software dashboard design

PactBloom is an innovative modern SaaS (software as a service) solution for contract and meeting management.

What we are looking for is fresh ideas for our dashboard. We do not need web coding or actionable wireframes now – but purely great design ideas from where to continue forward.

How should a modern web software dashboard look like? Fresh, intuitive, easy-to-use, and adaptable for responsive mobile designs. We hope that when the user logs into the service and sees the dashboard, he/she gets a good big picture of the current status of the most important documents of his/hers company.

To get to know the service and see the components, we kindly ask you to register to our service at www.pactbloom-demo.net and to utilize the free trial (30 days) so you can see the existing dashboard live. And also try out how it works. Might help you to get ideas how to improve it.

(The designer we will choose might be offered later on to design some other pages as well (contract view and edit pages, meeting page etc).)

You’ll find additional information in the attachment.

You’ll find more information of the company and the service also at www.pactbloom-demo.net

Target Market(s)

Global

Industry/Entity Type

Business Management

Number of Pages Required

1 page

Font styles to use
Sans Serif

Requirements
Must have
• 1) Clear design idea for us to iterate from, 2) Modern look and feel - elegant & bold at the same time - still with credibility in our target group. And 3) Suitable for dashboard usage - it should it a clear big picture for the user.
• UPDATE:
• Users should see most important things with one glance. Therefore we would like to see AT LEAST these items mentioned below on the first page.
• NOTE: if all these things are visible on the dashboard, the menu list is maybe not needed on the left. (And there might be some icons on the top header with needed settings/inbox features anyway.)
• NOTE2: as explained earlier, the design should be responsive i.e. work without modifications in PC, iPad and mobile (the areas/boxes would just rearrange themselves on top of each other.)
• -First area should be Documents, which would include different document categories: Contracts, Finance & Admin and HR
• -All different types of Meetings could be the next area (upcoming ones clearly visible with date and maybe description, time and location visible also).
• -Reminders and Activity Feed (they might also be together in top of each other, so that Reminder is visible first and Activity feed can be chosen from the tab.)
• -Virtual Datarooms (maybe 1-3 different ones with some analytics for each visible e.g. like usage/visits per day)
• Saved searches in very important list as users can save their most important searches. There are typically many of these, so at least 5 should be visible and then see all button (maybe even more could be visible if they fit on your design)
• My Latest is also important.
• (As explained, Action Required area is NOT needed anymore).
Nice to have
• Surprise us!
Should not have
• Please avoid the boring traditional legacy stuff and the common report dashboards.
• You do not need design a 100% mockup for the techie to continue with. The ideas count.

```html
<!DOCTYPE html>
<html lang="en">
<head>
<meta charset="utf-8">
<title>PactBloom Dashboard</title>
<link href="https://fonts.googleapis.com/css2?family=Open+Sans:wght@400;600;700&display=swap" rel="stylesheet">
<style>
:root{
  --black:#000;
  --green:#7cc242;
  --green-light:#8fd14f;
  --green-dark:#62a92e;
  --panel:rgba(58,58,58,.9);
  --side:rgba(34,34,34,.88);
  --text:#fff;
  --muted:#d8d8d8;
  --line:rgba(255,255,255,.28);
}
*{box-sizing:border-box;margin:0;padding:0}
html,body{width:1200px;height:988px;overflow:hidden;background:var(--black)}
body{font-family:"Open Sans",Arial,sans-serif;color:var(--text);position:relative}
.abs{position:absolute}
.topbar{left:0;top:0;width:1200px;height:83px;background:var(--black)}
.brand{left:25px;top:22px;display:flex;align-items:center;gap:10px;font-size:21px;font-weight:600;letter-spacing:.5px}
.brand .dot{width:34px;height:34px;border-radius:50%;background:var(--green)}
.search{left:333px;top:23px;width:372px;height:39px;border:1px solid #777;border-radius:20px;background:#111;display:flex;align-items:center;justify-content:space-between;padding:0 12px 0 14px;font-size:13px;color:#aaa}
.user{left:743px;top:18px;display:flex;align-items:center;gap:10px}
.avatar{width:45px;height:45px;border-radius:50%;border:3px solid var(--green);background:linear-gradient(#555,#2a2a2a)}
.user-name{font-size:13px;font-weight:600}
.user-co{font-size:11px;color:var(--muted)}
.auth{left:938px;top:31px;font-size:13px}
.auth span{color:var(--green)}
.backdrop{left:0;top:83px;width:1200px;height:820px;background:linear-gradient(135deg,#8a8a8a 0%,#c9c9c9 40%,#5e5e5e 75%,#9a9a9a 100%)}
.sidebar{left:0;top:83px;width:155px;height:820px;background:var(--side);border-right:1px solid #555}
.nav-item{position:absolute;left:0;width:155px;text-align:center;font-size:13px;line-height:24px}
.nav-item svg{display:block;margin:0 auto 2px}
.nav-item.active{color:var(--green)}
.panel{background:var(--panel)}
.panel-head{height:48px;background:linear-gradient(var(--green-light),var(--green-dark));display:flex;align-items:center;gap:12px;padding:0 16px;font-size:17px;text-transform:uppercase}
.meetings{left:183px;top:145px;width:558px;height:720px}
.meeting{position:absolute;left:8px;right:10px;border-bottom:1px solid var(--line);height:146px}
.date-badge{position:absolute;left:8px;top:27px;width:74px;height:71px;border:3px solid var(--green);border-radius:9px;text-align:center;font-size:16px;line-height:17px;padding-top:5px}
.meeting-title{position:absolute;left:97px;top:37px;font-size:18px}
.meeting-text{position:absolute;left:97px;top:65px;font-size:12.5px;color:var(--muted)}
.meeting-actions{position:absolute;right:0;top:109px;font-size:13px;display:flex;gap:10px;align-items:center}
.meeting-actions .sep{color:#888}
.plus{color:var(--green);font-size:15px}
.btn{position:absolute;width:97px;height:34px;border-radius:9px;background:linear-gradient(var(--green-light),var(--green-dark));font-size:12.5px;font-weight:700;display:flex;align-items:center;justify-content:center}
.reminders{left:766px;top:145px;width:414px;height:347px}
.reminder{position:absolute;left:25px;width:364px;height:96px;border:1px solid var(--line);border-radius:9px;padding:12px 10px}
.rem-date{color:var(--green);font-size:13px}
.rem-on{position:absolute;right:14px;top:12px;font-size:10.5px;font-weight:700;display:flex;align-items:center;gap:8px}
.rem-on i{width:9px;height:9px;border-radius:50%;background:var(--green)}
.rem-text{font-size:11px;line-height:18px;margin-top:9px}
.activity{left:766px;top:517px;width:414px;height:348px}
.activity .panel-head{justify-content:space-between}
.feed{position:absolute;width:179px;height:96px;border:1px solid var(--line);border-radius:9px}
.feed-photo{position:absolute;left:7px;top:7px;width:45px;height:45px;border:2px solid var(--green);background:linear-gradient(#bfbfbf,#6f6f6f)}
.feed-name{position:absolute;left:58px;top:16px;font-size:10px;color:var(--green);line-height:12px}
.feed-name span{display:block;color:#aaa}
.feed-chat{position:absolute;right:8px;top:16px}
.feed-text{position:absolute;left:7px;top:60px;font-size:11px}
.feed-time{position:absolute;font-size:10.5px}
.footer{left:0;top:903px;width:1200px;height:85px;background:var(--black);font-size:12.5px;font-weight:600;text-align:center;padding-top:37px}
.page-no{position:absolute;right:20px;top:40px;font-size:10px;font-weight:400}
</style>
</head>
<body>
<header class="topbar abs">
  <div class="brand abs"><span class="dot"></span>PactBloom</div>
  <div class="search abs">Search
    <svg width="22" height="22" viewBox="0 0 22 22" fill="none" stroke="#fff" stroke-width="1.6"><circle cx="9" cy="9" r="7"/><path d="M14 14l6 6"/></svg>
  </div>
  <div class="user abs">
    <div class="avatar" role="img" aria-label="User profile photo"></div>
    <div><div class="user-name">Daniel Hartley</div><div class="user-co">Company Name</div></div>
  </div>
  <div class="auth abs">Sign In <span>| Register</span></div>
</header>

<div class="backdrop abs" role="img" aria-label="Background photo of a desk with laptop and coffee cup"></div>

<nav class="sidebar abs">
  <div class="nav-item active" style="top:32px">
    <svg width="24" height="30" viewBox="0 0 24 30" fill="none" stroke="#7cc242" stroke-width="1.5"><rect x="2" y="4" width="20" height="24" rx="1"/><rect x="7" y="1" width="10" height="5"/><path d="M6 12l2 2 3-3M6 18l2 2 3-3M6 24l2 2 3-3M13 13h6M13 19h6M13 25h6"/></svg>Contracts</div>
  <div class="nav-item" style="top:106px">
    <svg width="38" height="34" viewBox="0 0 38 34" fill="none" stroke="#fff" stroke-width="1.5"><ellipse cx="19" cy="21" rx="15" ry="10"/><circle cx="19" cy="7" r="5"/><path d="M10 29v4M28 29v4M34 19h3"/></svg>Finance &amp;<br>Admin documents</div>
  <div class="nav-item" style="top:206px">
    <svg width="34" height="28" viewBox="0 0 34 28" fill="none" stroke="#fff" stroke-width="1.5"><rect x="1" y="3" width="32" height="24"/><path d="M8 3v24M22 12h8M22 17h8M22 22h8"/><rect x="14" y="12" width="6" height="10"/></svg>HR documents</div>
  <div class="nav-item" style="top:292px">
    <svg width="28" height="36" viewBox="0 0 28 36" fill="none" stroke="#fff" stroke-width="1.5"><rect x="2" y="3" width="24" height="32"/><path d="M6 1v4M10 1v4M14 1v4M18 1v4M22 1v4M6 12l2 2 3-3M6 19l2 2 3-3M6 26l2 2 3-3M13 13h9M13 20h9M13 27h9"/></svg>Company Register</div>
  <div class="nav-item" style="top:380px">
    <svg width="24" height="32" viewBox="0 0 24 32" fill="none" stroke="#fff" stroke-width="1.5"><rect x="2" y="2" width="20" height="28"/><path d="M2 8h20M12 13v10M7 18h10"/></svg>Virtual data rooms</div>
  <div class="nav-item" style="top:466px">
    <svg width="30" height="30" viewBox="0 0 30 30" fill="none" stroke="#fff" stroke-width="1.5"><path d="M15 3C8 3 3 7.5 3 13c0 3 1.5 5.6 4 7.4L6 27l6-4c1 .2 2 .3 3 .3 7 0 12-4.5 12-10.3S22 3 15 3z"/><path d="M9 11h12M9 15h12"/></svg>Meetings</div>
  <div class="nav-item" style="top:555px">
    <svg width="32" height="26" viewBox="0 0 32 26" fill="none" stroke="#fff" stroke-width="1.5"><circle cx="8" cy="18" r="6"/><circle cx="24" cy="18" r="6"/><path d="M5 12l3-10h4l1 10M27 12l-3-10h-4l-1 10M13 15h6"/></svg>Saved Searches</div>
  <div class="nav-item" style="top:642px">
    <svg width="26" height="32" viewBox="0 0 26 32" fill="none" stroke="#fff" stroke-width="1.5"><path d="M2 2h16l6 6v22H2z"/><path d="M18 2v6h6M13 12v11M8 18l5 5 5-5"/></svg>My Latest</div>
</nav>

<section class="meetings panel abs">
  <div class="panel-head">
    <svg width="24" height="22" viewBox="0 0 24 22" fill="none" stroke="#fff" stroke-width="1.4"><circle cx="13" cy="7" r="5"/><path d="M3 21c0-5 4-8 10-8s10 3 10 8z"/><path d="M7 4a5 5 0 0 0 0 8"/></svg>Meetings</div>
  <div class="meeting" style="top:48px;height:149px">
    <div class="date-badge">23rd<br>June<br>2016</div>
    <div class="meeting-title">Board Meetings</div>
    <div class="meeting-text">Neque porro quisquam est qui dolorem ipsum quia dolor sit &nbsp;elit...</div>
    <div class="meeting-actions"><span class="plus">⊞</span>Add <span class="sep">|</span><span class="plus">◉</span>View All</div>
  </div>
  <div class="meeting" style="top:197px;height:141px">
    <div class="date-badge" style="top:22px">23rd<br>June<br>2016</div>
    <div class="meeting-title" style="top:32px">Board Meetings</div>
    <div class="meeting-text" style="top:60px">Neque porro quisquam est qui dolorem ipsum quia dolor sit &nbsp;elit...</div>
    <div class="meeting-actions" style="top:104px"><span class="plus">⊞</span>Add <span class="sep">|</span><span class="plus">◉</span>View All</div>
  </div>
  <div class="meeting" style="top:338px;height:150px">
    <div class="date-badge" style="top:29px">23rd<br>June<br>2016</div>
    <div class="meeting-title" style="top:39px">Board Meetings</div>
    <div class="meeting-text" style="top:67px">Neque porro quisquam est qui dolorem ipsum quia dolor sit &nbsp;elit...</div>
    <div class="meeting-actions" style="top:112px"><span class="plus">⊞</span>Add <span class="sep">|</span><span class="plus">◉</span>View All</div>
  </div>
  <div class="meeting" style="top:488px;height:157px">
    <div class="date-badge" style="top:35px">23rd<br>June<br>2016</div>
    <div class="meeting-title" style="top:44px">Board Meetings</div>
    <div class="meeting-text" style="top:72px">Neque porro quisquam est qui dolorem ipsum quia dolor sit &nbsp;elit...</div>
    <div class="meeting-actions" style="top:120px"><span class="plus">⊞</span>Add <span class="sep">|</span><span class="plus">◉</span>View All</div>
  </div>
  <div class="btn" style="left:452px;top:671px">SEE ALL</div>
</section>

<section class="reminders panel abs">
  <div class="panel-head" style="gap:26px">
    <svg width="26" height="24" viewBox="0 0 26 24" fill="none" stroke="#fff" stroke-width="1.4"><path d="M13 2c-5 0-7 4-7 9v5l-3 4h20l-3-4v-5c0-5-2-9-7-9z"/><path d="M10 21a3 3 0 0 0 6 0"/></svg>Reminders</div>
  <div class="reminder" style="top:74px">
    <div class="rem-date">JUN 28TH | 2015</div>
    <div class="rem-on">REMINDER ON <i></i></div>
    <div class="rem-text">Neque porro quisquam est qui dolorem ipsum quia dolor sit amet, consectetur, adipisci velit...</div>
  </div>
  <div class="reminder" style="top:179px">
    <div class="rem-date">JUN 28TH | 2015</div>
    <div class="rem-on">REMINDER ON <i></i></div>
    <div class="rem-text">Neque porro quisquam est qui dolorem ipsum quia dolor sit amet, consectetur, adipisci velit...</div>
  </div>
  <svg class="abs" style="left:24px;top:301px" width="22" height="23" viewBox="0 0 22 23" fill="none" stroke="#fff" stroke-width="1.2"><rect x="1" y="3" width="20" height="19"/><path d="M1 7h20M5 1v4M9 1v4M13 1v4M17 1v4"/><text x="4" y="19" fill="#fff" stroke="none" font-size="10" font-family="Open Sans,sans-serif">18</text></svg>
  <div class="btn" style="left:293px;top:292px">SEE ALL</div>
</section>

<section class="activity panel abs">
  <div class="panel-head">
    <span style="display:flex;align-items:center;gap:14px">
    <svg width="26" height="22" viewBox="0 0 26 22" fill="none" stroke="#fff" stroke-width="1.4"><path d="M1 3h8l2 3h12v14H1z"/><path d="M1 20l4-10h20l-2 10"/></svg>Activity Feeds</span>
    <span style="font-size:18px;font-weight:700">‹ ›</span></div>

  <div class="feed" style="left:25px;top:80px">
    <div class="feed-photo" role="img" aria-label="Team member photo"></div>
    <div class="feed-name">Daniel Hartley<span>June 23rd | 2016</span></div>
    <svg class="feed-chat" width="26" height="24" viewBox="0 0 26 24" fill="none" stroke="#fff" stroke-width="1.3"><path d="M13 2C6.5 2 2 5.8 2 10.5c0 2.5 1.3 4.7 3.5 6.2L5 22l5-3c1 .2 2 .3 3 .3 6.5 0 11-3.8 11-8.6S19.5 2 13 2z"/><circle cx="8" cy="10.5" r=".8"/><circle cx="13" cy="10.5" r=".8"/><circle cx="18" cy="10.5" r=".8"/></svg>
    <div class="feed-text">Neque porro quisquam est...</div>
  </div>
  <div class="feed-time" style="left:145px;top:181px">2hr 2mints</div>

  <div class="feed" style="left:207px;top:80px">
    <div class="feed-photo" role="img" aria-label="Team member photo"></div>
    <div class="feed-name">Daniel Hartley<span>June 23rd | 2016</span></div>
    <svg class="feed-chat" width="26" height="24" viewBox="0 0 26 24" fill="none" stroke="#fff" stroke-width="1.3"><path d="M13 2C6.5 2 2 5.8 2 10.5c0 2.5 1.3 4.7 3.5 6.2L5 22l5-3c1 .2 2 .3 3 .3 6.5 0 11-3.8 11-8.6S19.5 2 13 2z"/><circle cx="8" cy="10.5" r=".8"/><circle cx="13" cy="10.5" r=".8"/><circle cx="18" cy="10.5" r=".8"/></svg>
    <div class="feed-text">Neque porro quisquam est...</div>
  </div>
  <div class="feed-time" style="left:327px;top:181px">2hr 2mints</div>

  <div class="feed" style="left:25px;top:210px">
    <div class="feed-photo" role="img" aria-label="Team member photo"></div>
    <div class="feed-name">Daniel Hartley<span>June 23rd | 2016</span></div>
    <svg class="feed-chat" width="26" height="24" viewBox="0 0 26 24" fill="none" stroke="#fff" stroke-width="1.3"><path d="M13 2C6.5 2 2 5.8 2 10.5c0 2.5 1.3 4.7 3.5 6.2L5 22l5-3c1 .2 2 .3 3 .3 6.5 0 11-3.8 11-8.6S19.5 2 13 2z"/><circle cx="8" cy="10.5" r=".8"/><circle cx="13" cy="10.5" r=".8"/><circle cx="18" cy="10.5" r=".8"/></svg>
    <div class="feed-text">Neque porro quisquam est...</div>
  </div>
  <div class="feed-time" style="left:145px;top:311px">2hr 2mints</div>

  <div class="feed" style="left:207px;top:210px">
    <div class="feed-photo" role="img" aria-label="Team member photo"></div>
    <div class="feed-name">Daniel Hartley<span>June 23rd | 2016</span></div>
    <svg class="feed-chat" width="26" height="24" viewBox="0 0 26 24" fill="none" stroke="#fff" stroke-width="1.3"><path d="M13 2C6.5 2 2 5.8 2 10.5c0 2.5 1.3 4.7 3.5 6.2L5 22l5-3c1 .2 2 .3 3 .3 6.5 0 11-3.8 11-8.6S19.5 2 13 2z"/><circle cx="8" cy="10.5" r=".8"/><circle cx="13" cy="10.5" r=".8"/><circle cx="18" cy="10.5" r=".8"/></svg>
    <div class="feed-text">Neque porro quisquam est...</div>
  </div>
  <div class="feed-time" style="left:327px;top:311px">2hr 2mints</div>
</section>

<footer class="footer abs">© 2016 COMPANY NAME &nbsp;| &nbsp; ALL RIGHTS RESERVED<span class="page-no">C5</span></footer>
</body>
</html>
```